Criação de Papelaria (6 itens) para Associações, ONGs ou Comunidades
" TORVI coordena recursos e competências com parceiros que realizam ações nos âmbitos da deficiência física e mental/intelectual, e dos jovens socialmente vulneráveis. TORVI apoia ações para e com as pessoas com deficiência, focando na inclusão social e no empoderamento, em especial maneira na formação profissional. TORVI apoia crianças e adolescentes socialmente vulneráveis (e as relativas famílias) realizando atividades nos setores de saúde, educação e cultura. O nome da organização manda à ideia de colocar-se em ação em relação ao apoio a projetos e programas sociais e de saúde no sentido amplo do termo. TORVI foi escolhido porque manda ao fogo, à ação, algo que faz acontecer, com carinho típico de quem cozinha, assa. "

```html
<!DOCTYPE html>
<html lang="pt-BR">
<head>
<meta charset="UTF-8">
<title>TORVI — Envelopes</title>
<link rel="stylesheet" href="https://fonts.googleapis.com/css2?family=Montserrat:wght@800&family=Tinos&display=swap">
<style>
  :root {
    --bg: #ecebe8;
    --paper: #ffffff;
    --paper-shade: #f1f1f1;
    --red: #b11d22;
    --red-dark: #8e1418;
    --red-light: #c8262c;
    --gray: #58585a;
    --line: #d6d6d6;
    --ink: #2b2b2b;
  }
  html, body {
    margin: 0;
    padding: 0;
    width: 1200px;
    height: 1200px;
    overflow: hidden;
    background: var(--bg);
  }
  .canvas {
    position: relative;
    width: 1200px;
    height: 1200px;
  }
  .envelope {
    position: absolute;
    left: 100px;
    width: 1000px;
    height: 490px;
    box-shadow: 0 6px 18px rgba(0,0,0,0.18);
    overflow: hidden;
  }
  .envelope--back { top: 70px; background: var(--paper); }
  .envelope--front { top: 640px; background: var(--red); }
  .envelope svg.art {
    position: absolute;
    inset: 0;
    width: 1000px;
    height: 490px;
  }
  .brand {
    position: absolute;
    display: flex;
    align-items: center;
    gap: 14px;
    font-family: "Montserrat", sans-serif;
    font-weight: 800;
    letter-spacing: 1px;
    line-height: 1;
  }
  .envelope--back .brand {
    left: 52px;
    top: 208px;
    font-size: 40px;
    color: var(--red);
  }
  .envelope--front .brand {
    left: 82px;
    top: 80px;
    font-size: 58px;
    color: var(--paper);
  }
  .brand-dot {
    width: 58px;
    height: 58px;
    border-radius: 50%;
    background: var(--paper);
  }
  .contact {
    position: absolute;
    right: 34px;
    top: 150px;
    margin: 0;
    padding: 0;
    list-style: none;
    font-family: "Tinos", serif;
    font-size: 15px;
    color: var(--ink);
  }
  .contact li {
    display: flex;
    justify-content: flex-end;
    align-items: center;
    gap: 14px;
    height: 30px;
  }
  .contact svg { width: 16px; height: 16px; flex: none; }
</style>
</head>
<body>
<main class="canvas">

  <section class="envelope envelope--back" aria-label="Verso do envelope">
    <svg class="art" viewBox="0 0 1000 490" aria-hidden="true">
      <defs>
        <linearGradient id="flapShade" x1="0" y1="0" x2="0" y2="1">
          <stop offset="0" stop-color="#ffffff"/>
          <stop offset="1" stop-color="#f3f3f3"/>
        </linearGradient>
      </defs>
      <path class="flap" d="M0,0 L470,178 Q500,190 530,178 L1000,0 Z" fill="url(#flapShade)" stroke="var(--line)" stroke-width="2"/>
      <path class="flap-shadow" d="M0,4 L470,184 Q500,196 530,184 L1000,4" fill="none" stroke="rgba(0,0,0,0.06)" stroke-width="4"/>
      <path class="wave-gray" d="M0,385 C230,345 430,430 640,425 C800,420 900,392 1000,372 L1000,490 L0,490 Z" fill="var(--gray)"/>
      <path class="wave-gap" d="M0,405 C230,368 430,452 640,446 C800,441 900,414 1000,394 L1000,490 L0,490 Z" fill="var(--paper)"/>
      <path class="wave-red" d="M0,414 C230,378 430,462 640,456 C800,451 900,425 1000,405 L1000,490 L0,490 Z" fill="var(--red)"/>
      <path class="wave-red-deep" d="M0,455 C260,430 470,490 700,485 L0,490 Z" fill="var(--red-dark)" opacity="0.5"/>
    </svg>

    <div class="brand">TORVI</div>

    <ul class="contact">
      <li>Endereço completo - Cidade - Estado
        <svg viewBox="0 0 16 16"><path d="M8 1a5 5 0 0 0-5 5c0 4 5 9 5 9s5-5 5-9a5 5 0 0 0-5-5zm0 7a2 2 0 1 1 0-4 2 2 0 0 1 0 4z" fill="var(--red)"/></svg></li>
      <li>(00) 0000-0000 | (00) 000000-0000
        <svg viewBox="0 0 16 16"><path d="M2 5c0-2 2-3 6-3s6 1 6 3v1h-3V5H5v1H2zM3 8h10l1 6H2z" fill="var(--red)"/></svg></li>
      <li>(00) 0000-0000 | (00) 000000-0000
        <svg viewBox="0 0 16 16"><rect x="4" y="1" width="8" height="14" rx="1.5" fill="var(--red)"/><rect x="5.5" y="3" width="5" height="8" fill="#fff"/></svg></li>
      <li>seuemail@seuemail.com.br
        <svg viewBox="0 0 16 16"><rect x="1" y="3" width="14" height="10" rx="1" fill="var(--red)"/><path d="M1.5 4 8 9l6.5-5" fill="none" stroke="#fff" stroke-width="1.3"/></svg></li>
      <li>www.torviacao.org.br
        <svg viewBox="0 0 16 16"><circle cx="8" cy="8" r="7" fill="var(--red)"/><path d="M1 8h14M8 1c-3 3-3 11 0 14M8 1c3 3 3 11 0 14" fill="none" stroke="#fff" stroke-width="1"/></svg></li>
    </ul>
  </section>

  <section class="envelope envelope--front" aria-label="Frente do envelope">
    <svg class="art" viewBox="0 0 1000 490" aria-hidden="true">
      <defs>
        <radialGradient id="redGlow" cx="0.45" cy="0.4" r="0.7">
          <stop offset="0" stop-color="var(--red-light)"/>
          <stop offset="1" stop-color="var(--red-dark)"/>
        </radialGradient>
      </defs>
      <rect width="1000" height="490" fill="url(#redGlow)"/>
      <path class="wave-white" d="M0,390 C220,380 420,445 640,440 C800,436 900,412 1000,395 L1000,490 L0,490 Z" fill="var(--paper)"/>
      <path class="wave-gray" d="M0,420 C240,400 440,470 660,462 C810,457 910,432 1000,418 L1000,490 L0,490 Z" fill="var(--gray)"/>
      <path class="wave-gap" d="M0,440 C240,420 440,484 660,477 C810,472 910,448 1000,434 L1000,490 L0,490 Z" fill="var(--paper)"/>
      <path class="wave-red" d="M0,450 C240,432 440,490 660,486 C810,483 910,460 1000,446 L1000,490 L0,490 Z" fill="var(--red)"/>
    </svg>

    <div class="brand"><span class="brand-dot"></span>TORVI</div>
  </section>

</main>
</body>
</html>
```